GPB New Busines Card

we need a business card for or renovation company, our main color is orange and our logo is a concrete ball rolling with GPB on it.the company name is Granite Path Builders, Inc, we need somthing simple but profecional, also that we can change if its for roofing or renovations and the names

Target Market(s)

home owners

Industry/Entity Type

Concrete

Contact Information for Business Card

Colors
f68d4d
f9ba93
f37122
f78f20
faa54b
fbc994

```html
<!DOCTYPE html>
<html lang="en">
<head>
<meta charset="utf-8">
<title>Granite Path Builders – Business Card</title>
<link href="https://fonts.googleapis.com/css2?family=Libre+Baskerville:wght@400;700&family=Open+Sans:wght@400;600&display=swap" rel="stylesheet">
<style>
  :root {
    --orange-deep: #f37122;
    --orange: #f78f20;
    --orange-soft: #faa54b;
    --orange-pale: #fbc994;
    --peach: #f9ba93;
    --brown: #4a2a12;
    --ink: #1d1d1d;
    --grey-ball: #a9a39c;
    --paper: #ffffff;
    --stage: #e9e6e2;
  }
  * { margin: 0; padding: 0; box-sizing: border-box; }
  html, body { width: 1200px; height: 906px; overflow: hidden; }
  body {
    background: var(--stage);
    display: flex; flex-direction: column; align-items: center; justify-content: center;
    gap: 44px;
    font-family: "Open Sans", Arial, sans-serif;
  }
  .card {
    position: relative; width: 640px; height: 366px; overflow: hidden;
    box-shadow: 0 6px 18px rgba(0,0,0,.18);
  }

  /* front */
  .card-front { background: var(--paper); }
  .brand {
    position: absolute; left: 60px; top: 70px;
    display: flex; align-items: center; gap: 22px;
  }
  .brand-ball { width: 96px; height: 96px; border-radius: 50%; background: var(--grey-ball); }
  .brand-name {
    font-family: "Libre Baskerville", Georgia, serif; font-weight: 700;
    font-size: 34px; color: var(--ink); line-height: 1.1;
  }
  .service-band {
    position: absolute; left: 0; right: 0; top: 214px; height: 58px;
    background: var(--orange);
    display: flex; align-items: center; padding-left: 60px;
  }
  .service-band::before {
    content: ""; position: absolute; left: 0; top: 0; bottom: 0; width: 28px;
    background: var(--orange-soft);
  }
  .service-list {
    font-family: "Libre Baskerville", Georgia, serif; font-size: 24px; color: var(--paper);
  }
  .front-note {
    position: absolute; right: 34px; bottom: 28px;
    font-family: "Libre Baskerville", Georgia, serif; font-size: 13px; color: var(--ink);
  }

  /* back */
  .card-back {
    background: linear-gradient(135deg, var(--orange-deep) 0%, var(--orange) 100%);
    color: var(--paper);
  }
  .accent-tab {
    position: absolute; left: 250px; top: 0; width: 90px; height: 22px;
    background: var(--orange-soft);
  }
  .name-block {
    position: absolute; left: 0; top: 40px; width: 250px; height: 96px;
    background: rgba(249,186,147,.45);
    padding: 18px 0 0 30px;
  }
  .person-name {
    font-family: "Libre Baskerville", Georgia, serif; font-weight: 700;
    font-size: 30px; color: var(--brown); white-space: nowrap;
  }
  .person-role { font-size: 14px; margin-top: 6px; color: var(--paper); }
  .contact {
    position: absolute; left: 30px; top: 168px;
    display: flex; gap: 24px;
  }
  .contact-icons { display: flex; flex-direction: column; gap: 8px; padding-top: 1px; }
  .contact-icons svg { width: 21px; height: 21px; display: block; }
  .contact-lines { list-style: none; font-size: 16px; line-height: 29px; }
</style>
</head>
<body>

<section class="card card-front" aria-label="Card front">
  <div class="brand">
    <span class="brand-ball"></span>
    <span class="brand-name">Granite Path<br>Builders</span>
  </div>
  <div class="service-band"><span class="service-list">Roofing, Painting, Renovation</span></div>
  <p class="front-note">Free Estimates Licensed &amp; Insured</p>
</section>

<section class="card card-back" aria-label="Card back">
  <span class="accent-tab"></span>
  <div class="name-block">
    <h1 class="person-name">Marisol Ortega</h1>
    <p class="person-role">Sales Representative</p>
  </div>
  <div class="contact">
    <div class="contact-icons" aria-hidden="true">
      <svg viewBox="0 0 20 20"><circle cx="10" cy="10" r="9" fill="none" stroke="#fff" stroke-width="1.4"/><path d="M7 6l2 2-1 1.2c.6 1.3 1.5 2.2 2.8 2.8L12 11l2 2-1.3 1.3C9.5 14 6 10.5 5.7 7.3z" fill="#fff"/></svg>
      <svg viewBox="0 0 20 20"><circle cx="10" cy="10" r="9" fill="none" stroke="#fff" stroke-width="1.4"/><rect x="7.2" y="5" width="5.6" height="10" rx="1" fill="#fff"/></svg>
      <svg viewBox="0 0 20 20"><circle cx="10" cy="10" r="9" fill="none" stroke="#fff" stroke-width="1.4"/><rect x="5.5" y="8" width="9" height="6" fill="#fff"/><rect x="7" y="5" width="6" height="3" fill="#fff"/></svg>
      <svg viewBox="0 0 20 20"><circle cx="10" cy="10" r="9" fill="none" stroke="#fff" stroke-width="1.4"/><circle cx="10" cy="10" r="5" fill="none" stroke="#fff" stroke-width="1.2"/><path d="M5 10h10M10 5v10" stroke="#fff" stroke-width="1"/></svg>
      <svg viewBox="0 0 20 20"><circle cx="10" cy="10" r="9" fill="none" stroke="#fff" stroke-width="1.4"/><rect x="5" y="6.5" width="10" height="7" fill="#fff"/><path d="M5 6.5l5 4 5-4" stroke="#f37122" stroke-width="1" fill="none"/></svg>
      <svg viewBox="0 0 20 20"><circle cx="10" cy="10" r="9" fill="none" stroke="#fff" stroke-width="1.4"/><path d="M10 15s-4-4-4-6.5a4 4 0 018 0C14 11 10 15 10 15z" fill="#fff"/><circle cx="10" cy="8.5" r="1.4" fill="#f37122"/></svg>
    </div>
    <ul class="contact-lines">
      <li>+404-555-0142</li>
      <li>+770-555-0187</li>
      <li>+770-555-0163</li>
      <li>www.granitepathbuilders.com</li>
      <li>Marisol@GranitePathBuilders.com</li>
      <li>418 Maple Crest Ln Dacula, GA 30019</li>
    </ul>
  </div>
</section>

</body>
</html>
```